curtainmaker, indoor and outdoor blind supplier

looking for logo to use for business cards and letter heads, I make all curtains for my clients and supply all kinds of blinds indoor and out. I'm looking for a design maybe with fabric background,

Industry/Entity Type

Business

Contact Information for Business Card

Moira Delaney Curtain Designs 14 Perriwick Drive Kelsbrook 3915. phone 03 55847391 mobile 0428936054, email moiradelaneycurtaindesign@tarvomail.com website moiradelaneycurtaindesigns.example.au/

Requirements
Nice to have
• maybe something in relation to sewing as an option

```html
<!DOCTYPE html>
<html lang="en">
<head>
<meta charset="utf-8">
<title>Moira Delaney Curtain Designs – Business Card</title>
<link rel="stylesheet" href="https://fonts.googleapis.com/css2?family=Lato:wght@400;700&family=Pinyon+Script&display=swap">
<style>
  :root {
    --page: #ece6da;
    --leather-dark: #3f2718;
    --leather: #5b3b27;
    --leather-light: #73503a;
    --fabric-dark: #6e4f33;
    --fabric: #a57f58;
    --fabric-light: #cfb08a;
    --olive: #b6b45e;
    --olive-dark: #8d8b3f;
    --gold: #e2d89a;
    --cream: #f3ecd6;
    --ink-soft: #d9ccb0;
  }
  * { box-sizing: border-box; margin: 0; padding: 0; }
  html, body { width: 1200px; height: 1000px; overflow: hidden; }
  body {
    background: var(--page);
    font-family: "Lato", Arial, sans-serif;
    position: relative;
  }
  .card {
    position: absolute;
    width: 525px;
    height: 300px;
    border-radius: 6px;
    overflow: hidden;
    box-shadow: 0 10px 24px rgba(60, 40, 20, .28);
  }
  .card--front { left: 55px; top: 90px; background: radial-gradient(ellipse at 35% 30%, var(--leather-light), var(--leather) 55%, var(--leather-dark)); }
  .card--back { left: 620px; top: 90px; background: var(--leather); }

  .edge-strip { position: absolute; top: 0; bottom: 0; width: 18px; background: linear-gradient(90deg, var(--olive-dark), var(--olive)); }
  .card--front .edge-strip { right: 0; }
  .card--back .edge-strip { left: 0; }

  /* front */
  .brand-mark {
    position: absolute; left: 28px; top: 40px; width: 180px;
    display: flex; align-items: center; gap: 10px;
  }
  .brand-mark__square { width: 18px; height: 18px; flex: none; background: var(--gold); }
  .brand-mark__name { color: var(--gold); font-size: 19px; font-weight: 700; line-height: 1.2; }

  .contact { position: absolute; left: 240px; top: 34px; right: 40px; color: var(--cream); }
  .contact__name { font-size: 25px; font-weight: 700; color: var(--cream); }
  .contact__role { font-size: 14px; color: var(--ink-soft); margin-top: 2px; padding-bottom: 8px; border-bottom: 1px solid var(--olive); }
  .contact__list { list-style: none; margin-top: 9px; }
  .contact__item { display: flex; align-items: center; gap: 7px; font-size: 10.5px; line-height: 1.2; margin-bottom: 6px; white-space: nowrap; }
  .contact__icon { width: 15px; height: 15px; flex: none; }
  .contact__phones { display: flex; gap: 18px; }
  .contact__phones .contact__item { margin-bottom: 0; }

  .services-band {
    position: absolute; left: 0; right: 18px; bottom: 0; height: 62px;
    background: linear-gradient(180deg, var(--fabric-dark), var(--fabric) 50%, var(--fabric-dark));
    display: flex; align-items: center; justify-content: center;
    border-top: 2px solid var(--olive);
  }
  .services-band__art { position: absolute; inset: 0; }
  .services {
    position: relative; display: flex;
    font-family: "Pinyon Script", cursive; font-size: 25px; color: var(--cream);
  }
  .services span { padding: 0 22px; }
  .services span + span { border-left: 1px solid var(--gold); }

  /* back */
  .curtain-art {
    position: absolute; left: 18px; right: 0; top: 0; bottom: 0;
    background:
      linear-gradient(90deg, var(--fabric-dark), var(--fabric) 14%, transparent 30%, transparent 70%, var(--fabric) 86%, var(--fabric-dark)),
      linear-gradient(180deg, var(--fabric) 0%, var(--fabric-light) 22%, #b99772 60%, var(--fabric-dark));
  }
  .back-brand {
    position: absolute; left: 18px; right: 0; top: 92px;
    display: flex; justify-content: center; align-items: center; gap: 12px;
  }
  .back-brand__square { width: 22px; height: 22px; background: var(--leather-dark); }
  .back-brand__name { font-size: 24px; font-weight: 700; color: var(--leather-dark); }
  .back-rule { position: absolute; left: 90px; right: 72px; top: 150px; height: 1px; background: var(--leather-dark); opacity: .6; }
  .back-url { position: absolute; left: 18px; right: 0; bottom: 26px; text-align: center; font-size: 13px; color: var(--cream); letter-spacing: .3px; }

  /* standalone logo block */
  .logo-block {
    position: absolute; left: 300px; top: 500px; width: 600px; height: 400px;
    display: flex; flex-direction: column; align-items: center; justify-content: center; gap: 26px;
  }
  .logo-block__art {
    width: 300px; height: 230px; border-radius: 8px;
    background: linear-gradient(180deg, var(--fabric-dark), var(--fabric) 40%, var(--fabric-light) 60%, var(--fabric-dark));
    border: 3px solid var(--gold);
  }
  .logo-block__brand { display: flex; align-items: center; gap: 14px; }
  .logo-block__square { width: 26px; height: 26px; background: var(--leather); }
  .logo-block__name { font-size: 34px; font-weight: 700; color: var(--leather); }
</style>
</head>
<body>

<section class="card card--front" aria-label="Business card front">
  <div class="brand-mark">
    <span class="brand-mark__square"></span>
    <span class="brand-mark__name">Moira Delaney Curtain Designs</span>
  </div>

  <div class="contact">
    <h1 class="contact__name">Moira Delaney</h1>
    <p class="contact__role">Owner/Chief Designer</p>
    <ul class="contact__list">
      <li class="contact__item">
        <svg class="contact__icon" viewBox="0 0 16 16"><circle cx="8" cy="8" r="8" fill="#b6b45e"/><path d="M8 3.5a2.6 2.6 0 0 0-2.6 2.6C5.4 8.2 8 12 8 12s2.6-3.8 2.6-5.9A2.6 2.6 0 0 0 8 3.5z" fill="#3f2718"/><circle cx="8" cy="6.1" r=".9" fill="#b6b45e"/></svg>
        14 Perriwick Drive Kelsbrook 3915
      </li>
      <li class="contact__item">
        <svg class="contact__icon" viewBox="0 0 16 16"><circle cx="8" cy="8" r="8" fill="#b6b45e"/><rect x="4" y="5" width="8" height="6" fill="none" stroke="#3f2718" stroke-width="1.1"/><path d="M4 5l4 3.3L12 5" fill="none" stroke="#3f2718" stroke-width="1.1"/></svg>
        moiradelaneycurtaindesign@tarvomail.com
      </li>
      <li class="contact__item">
        <svg class="contact__icon" viewBox="0 0 16 16"><circle cx="8" cy="8" r="8" fill="#b6b45e"/><circle cx="8" cy="8" r="4" fill="none" stroke="#3f2718" stroke-width="1"/><path d="M4 8h8M8 4c-1.6 2.4-1.6 5.6 0 8M8 4c1.6 2.4 1.6 5.6 0 8" fill="none" stroke="#3f2718" stroke-width=".8"/></svg>
        moiradelaneycurtaindesigns.example.au/
      </li>
      <li class="contact__item contact__phones">
        <span class="contact__item">
          <svg class="contact__icon" viewBox="0 0 16 16"><circle cx="8" cy="8" r="8" fill="#b6b45e"/><path d="M5 4.2l1.6-.4 1 2.2-1 .8c.5 1.1 1.3 1.9 2.4 2.4l.8-1 2.2 1-.4 1.6C9 11 5 7 5 4.2z" fill="#3f2718"/></svg>
          03 55847391
        </span>
        <span class="contact__item">
          <svg class="contact__icon" viewBox="0 0 16 16"><circle cx="8" cy="8" r="8" fill="#b6b45e"/><rect x="5.6" y="3.5" width="4.8" height="9" rx=".8" fill="#3f2718"/><rect x="6.4" y="4.6" width="3.2" height="5.8" fill="#b6b45e"/></svg>
          0428936054
        </span>
      </li>
    </ul>
  </div>

  <div class="services-band">
    <div class="services-band__art" role="img" aria-label="Illustration of gathered curtain fabric with a tasselled tie-back"></div>
    <p class="services"><span>Curtains</span><span>Blinds</span><span>Outdoors</span></p>
  </div>
  <div class="edge-strip"></div>
</section>

<section class="card card--back" aria-label="Business card back">
  <div class="edge-strip"></div>
  <div class="curtain-art" role="img" aria-label="Illustration of drawn-back curtains with tassel tie-backs framing a window blind"></div>
  <div class="back-brand">
    <span class="back-brand__square"></span>
    <span class="back-brand__name">Moira Delaney Curtain Designs</span>
  </div>
  <div class="back-rule"></div>
  <p class="back-url">moiradelaneycurtaindesigns.example.au</p>
</section>

<section class="logo-block" aria-label="Brand logo">
  <div class="logo-block__art" role="img" aria-label="Illustration of theatre-style curtains with tassels framing a slatted blind"></div>
  <div class="logo-block__brand">
    <span class="logo-block__square"></span>
    <span class="logo-block__name">Moira Delaney Curtain Designs</span>
  </div>
</section>

</body>
</html>
```